Vantrelix Template Refresh 2017

We want software development managers to remember that presentations using this template showcased Vantrelix technology: Our template must be distinctive to be remembered as showing Vantrelix technology: They must stand out from the 100s of other tech presentations they see, without being 'wacky', but professional whether bold or subtle. We are targeting the world's largest corporations.

[What do we do?] Vantrelix offers the world's first objective, fair measure of software developer productivity (Vantrelix Keystroke Gauge) and code quality (Vantrelix DUX) metrics.

Our corporate colour is (hex) Red: 13, Green: 10, Blue: 74.

Target Market(s)

CIOs, CTOs and senior software development managers in large Enterprises.

Industry/Entity Type

Information Technology

Font styles to use
Sans Serif

Colors
0355a3

Requirements
Must have
• A memorable design
Nice to have
• Template for slides that will show a view of our User Interface (which shows graphs and charts); ideally a consistent theme to make it clear that this is our own UI, not general graphs and charts to illustrate the presentation. (None of the graphs and charts in the attached presentation are from our User Interface)
• A suggestion would be to make use of our "chord" shape (cut off circle in our logo). This could be white on a blue to appear as a cut-out window for the slide content.
Should not have
• A colourful / jokey / fun tone.

```html
<!DOCTYPE html>
<html lang="en">
<head>
<meta charset="utf-8">
<title>Vantrelix – Calculating Coding Effort</title>
<link rel="stylesheet" href="https://fonts.googleapis.com/css2?family=Barlow+Semi+Condensed:wght@700;800&family=Barlow:wght@500;700&display=swap">
<style>
  :root {
    --brand-blue: #0355a3;
    --brand-navy: #0d0a4a;
    --paper: #ffffff;
    --subhead-grey: #4a4a4a;
  }
  html, body {
    margin: 0;
    padding: 0;
    overflow: hidden;
    background: var(--paper);
  }
  .slide {
    position: relative;
    width: 1200px;
    height: 675px;
    overflow: hidden;
    background: var(--paper);
    font-family: "Barlow", Arial, sans-serif;
  }
  .slide__backdrop {
    position: absolute;
    inset: 0;
    width: 1200px;
    height: 675px;
  }
  .backdrop__wedge,
  .backdrop__ring { fill: var(--brand-blue); }
  .backdrop__window { fill: var(--paper); }

  .brand {
    position: absolute;
    top: 84px;
    right: 100px;
    margin: 0;
    font-family: "Barlow", Arial, sans-serif;
    font-weight: 700;
    font-size: 80px;
    line-height: 1;
    letter-spacing: -1px;
    color: var(--brand-navy);
  }

  .title-block {
    position: absolute;
    left: 153px;
    top: 352px;
    width: 500px;
    text-align: center;
  }
  .title-block__heading {
    margin: 0;
    font-family: "Barlow Semi Condensed", "Arial Narrow", sans-serif;
    font-weight: 800;
    font-size: 74px;
    line-height: 77px;
    color: var(--brand-blue);
    text-transform: uppercase;
  }
  .title-block__rule {
    width: 400px;
    margin: 26px auto 0;
    border: 0;
    border-top: 4px dotted var(--brand-blue);
  }
  .title-block__subheading {
    margin: 28px 0 0;
    font-weight: 500;
    font-size: 27px;
    letter-spacing: 1.6px;
    color: var(--subhead-grey);
  }
</style>
</head>
<body>
  <main class="slide">
    <svg class="slide__backdrop" viewBox="0 0 1280 720" aria-hidden="true">
      <polygon class="backdrop__wedge" points="0,0 20,0 725,720 0,720"/>
      <circle class="backdrop__ring" cx="432" cy="577" r="390"/>
      <circle class="backdrop__window" cx="432" cy="577" r="377"/>
    </svg>

    <p class="brand">Vantrelix</p>

    <section class="title-block">
      <h1 class="title-block__heading">Calculating<br>Coding Effort</h1>
      <hr class="title-block__rule">
      <p class="title-block__subheading">‘Subheader Goes Here If Needed’</p>
    </section>
  </main>
</body>
</html>
```